Vantor Baseball Athletic Training Brochure Design 3 Fold 8x8

I need to create a New 3 page folding brochure for an elite baseball training company that focuses on all aspects of becoming a better baseball player through athletic training. I would like it to be fresh and new. My client likes the Kelmford Harriers colors. It needs to appeal to a young athletic crowd.

HERE IS A WEBSITE FROM A COMPETITOR
https://www.pulvanfit.example/baseball/
I HAVE INCLUEDE A PDF FLYER OF SOMETHING THEIR COMPETITORS HAVE DONE

Target Market(s)

Professional and amateur baseball players

Font styles to use
Sans Serif

Colors
33a6d7
3176b5
000000
b2b2b2

Requirements
Must have
• Images featuring training. I would use BRAXWELD training images as well.
• References:
• "As a former professional baseball player, I know the hard work and dedication it takes to make it and be your best.
• Every athlete that aspires to be the best they can be must out work their opponents on all levels,
• especially when it comes to taking care of your body. Being strong physically is a must with all the
• elite athletes competing. To get an edge, you have to be on a program designed by en experienced trainer
• and leader. With that said, there's nobody I'd recommend higher than Dean Valcourt with Vantor's
• Training.
• -Colby Fenwick
• Founder Bright Arc Hitting
• 12 year Professional Veteran
• "Training at VT in the off-season had my body feeling the best it felt going into Spring Training. My power in hitting, my speed in running, and the quickness of my feet in the infield hadn’t felt this good in a long time."
• -Tobin Marquette, Professional Baseball Player
• "Dean is one of a handful of baseball-specific strength coaches that we choose to refer out to on the west coast when Halvik Sports Performance athletes are in search of quality supervision and an appreciation for the unique needs of this athletic population."
• Co-Owner of HSP, Gordon Ashby-
• "Having played at the professional level, I understand that the demands of the baseball season are tough and recovery is very important, but also realize the off-season is short and this not just a time to recover but get better."
• - Dean Valcourt Owner

```html
<!DOCTYPE html>
<html lang="en">
<head>
<meta charset="utf-8">
<title>Vantor Baseball Athletic Training – Tri-fold Brochure</title>
<link href="https://fonts.googleapis.com/css2?family=Oswald:wght@300;400;500&family=Roboto+Condensed:ital,wght@0,400;0,700;1,300;1,400;1,700&display=swap" rel="stylesheet">
<style>
  :root{
    --sky:#33a6d7;
    --blue:#3176b5;
    --band:#4b8cc2;
    --band-text:#2a5f96;
    --black:#000000;
    --grey:#b2b2b2;
    --panel-top:#3a3a3a;
    --panel-bottom:#1c1c1c;
    --white:#ffffff;
    --soft:#d6d6d6;
  }
  *{margin:0;padding:0;box-sizing:border-box}
  html,body{width:1200px;height:923px;overflow:hidden;background:var(--white)}
  body{position:relative;font-family:"Roboto Condensed",Arial,sans-serif;color:var(--white)}
  .spread{position:absolute;left:16px;width:1170px;height:390px;display:flex}
  .spread--outside{top:67px}
  .spread--inside{top:466px}
  .panel{position:relative;width:390px;height:390px;overflow:hidden;
    background:radial-gradient(ellipse at 50% 40%,var(--panel-top),var(--panel-bottom) 80%)}
  .abs{position:absolute}
  .photo{position:absolute}
  .brand-name{font-family:"Oswald",sans-serif;font-weight:500;color:var(--white);letter-spacing:3px;text-align:center;display:flex;align-items:center;justify-content:center;gap:6px}
  .brand-name .dot{width:8px;height:8px;background:var(--sky);display:inline-block}

  /* outside: owner quote */
  .owner-photo{left:0;top:0;width:115px;height:390px;background:linear-gradient(90deg,#6a6a6a,#3d3d3d 70%,transparent)}
  .owner-brand{left:150px;top:62px;width:120px;font-size:16px}
  .owner-quote{left:75px;top:135px;width:270px;text-align:center;font-style:italic;font-weight:300;font-size:13.5px;line-height:20.5px;font-family:"Roboto Condensed",sans-serif}
  .owner-quote strong{font-family:"Oswald",sans-serif;font-style:normal;font-weight:400;font-size:17px}
  .owner-name{left:90px;top:235px;width:240px;text-align:center;font-family:"Oswald",sans-serif;font-size:22px}
  .owner-role{left:90px;top:263px;width:240px;text-align:center;font-family:"Oswald",sans-serif;font-weight:300;font-size:12px}

  /* outside: testimonial */
  .gym-photo{inset:0;background:linear-gradient(160deg,#9a9a9a,#6c6c6c 45%,#3e3e3e)}
  .testimonial-box{left:5px;top:5px;width:175px;padding:5px 6px;background:rgba(51,166,215,.85);color:#14324a;font-weight:700;font-size:7.6px;line-height:8.4px;text-align:justify}
  .testimonial-box .hl{color:var(--white)}
  .testimonial-end{left:15px;top:305px;width:150px;font-size:9.5px;line-height:13px}
  .testimonial-end .hl{background:var(--blue);padding:0 2px}
  .testimonial-name{right:24px;top:352px;text-align:right;font-style:italic;font-weight:700;font-size:11px;line-height:12px}
  .testimonial-name span{font-size:8px}

  /* outside: cover */
  .cover-brand{left:0;top:0;width:390px;height:390px;font-size:62px;letter-spacing:8px;color:var(--blue)}

  /* inside: contact */
  .contact-brand{left:150px;top:60px;width:120px;font-size:16px}
  .contact-title{left:0;top:138px;width:390px;text-align:center;font-family:"Oswald",sans-serif;font-size:20px;line-height:24px}
  .contact-sub{left:0;top:162px;width:390px;text-align:center;font-family:"Oswald",sans-serif;font-size:15px}
  .contact-list{left:0;top:198px;width:390px;text-align:center;font-family:"Oswald",sans-serif;font-weight:300;font-size:12.5px;line-height:17px;list-style:none}
  .contact-web{left:0;top:370px;width:390px;text-align:center;font-family:"Oswald",sans-serif;font-weight:300;font-size:9px;letter-spacing:.5px}

  /* inside: services */
  .intro-box{left:13px;top:10px;width:172px;height:118px;background:var(--band);padding:8px 12px}
  .intro-box h2{font-family:"Oswald",sans-serif;font-weight:400;font-size:10.5px;line-height:11px;color:#10263d;margin-bottom:4px}
  .intro-box p{font-size:5.3px;line-height:7px;font-weight:700;color:var(--white)}
  .service-list{left:178px;top:45px;list-style:none;font-style:italic;font-size:11px;line-height:19px}
  .tools-title{left:0;top:152px;width:390px;text-align:center;font-family:"Oswald",sans-serif;font-weight:300;font-size:26px;transform:skewX(-8deg);color:var(--white)}
  .tools-band{left:0;top:182px;width:390px;height:112px;background:var(--band)}
  .tools-list{left:0;top:188px;width:390px;text-align:center;list-style:none;font-family:"Oswald",sans-serif;font-weight:300;font-style:italic;font-size:17px;line-height:20.5px;color:var(--band-text)}
  .tools-copy{left:205px;top:308px;width:172px;font-size:6.2px;line-height:8.8px;font-weight:700;color:var(--soft)}

  /* inside: what we do */
  .wwd-title{left:26px;top:10px;font-family:"Oswald",sans-serif;font-size:13px}
  .wwd-intro{left:26px;top:27px;width:350px;font-size:7px;line-height:8.2px;color:var(--soft)}
  .letters{display:flex;gap:2px}
  .letters span{display:inline-block;width:12px;height:14px;background:var(--white);color:var(--black);font-family:"Oswald",sans-serif;font-size:10px;line-height:14px;text-align:center}
  .pillar{left:178px;width:200px;font-size:6.8px;line-height:9px;color:var(--soft)}
  .pillar ul{list-style:none;margin-top:5px}
  .pillar li{position:relative;padding-left:11px;margin-bottom:3px}
  .pillar li::before{content:"";position:absolute;left:0;top:3px;width:4px;height:4px;background:var(--white)}
  .pillar p{margin-top:5px}
  .pillar--strength{top:91px}
  .pillar--power{top:183px}
  .pillar--explosive{top:295px}
  .wwd-tagline{left:15px;top:170px;width:160px;text-align:center;font-style:italic;font-weight:700;font-size:10px;line-height:12px;color:var(--sky)}
  .wwd-tagline strong{font-size:13.5px;line-height:18px}
  .batter-art{left:18px;top:236px;width:150px;height:146px;background:radial-gradient(ellipse at 50% 50%,#6a6a6a,transparent 70%)}
</style>
</head>
<body>

<section class="spread spread--outside">
  <article class="panel panel--owner">
    <div class="photo owner-photo" role="img" aria-label="Black and white photo of the owner lifting a medicine ball"></div>
    <div class="abs brand-name owner-brand"><span class="dot"></span>VANTOR</div>
    <p class="abs owner-quote">Having played at the professional level, I understand that the demands of the baseball season are <strong>tough</strong> and recovery is very important, but also realize the off-season is short and this not just a time to recover but <strong>get better</strong></p>
    <p class="abs owner-name">- Dean Valcourt -</p>
    <p class="abs owner-role">Owner</p>
  </article>

  <article class="panel panel--testimonial">
    <div class="photo gym-photo" role="img" aria-label="Black and white photo of a trainer coaching an athlete with a medicine ball in the gym"></div>
    <p class="abs testimonial-box">“ As a former <span class="hl">professional baseball</span> player, I know the hard work and dedication it takes to make it and be your best. <span class="hl">Every athlete</span> that aspires to be the best they can be must out work their opponents on all levels, especially when it comes to taking care of your body. Being strong physically is a must with all the elite athletes competing. To get an edge, you have to be on a program designed by en experienced trainer and leader.</p>
    <p class="abs testimonial-end">With that said, there’s nobody I’d recommend higher than <span class="hl">Dean Valcourt</span> with Vantor’s Training. ”</p>
    <p class="abs testimonial-name">- Colby Fenwick -<br><span>Founder Bright Arc Hitting</span></p>
  </article>

  <article class="panel panel--cover">
    <div class="abs brand-name cover-brand">VANTOR</div>
  </article>
</section>

<section class="spread spread--inside">
  <article class="panel panel--contact">
    <div class="abs brand-name contact-brand"><span class="dot"></span>VANTOR</div>
    <h2 class="abs contact-title">Let’s Start</h2>
    <p class="abs contact-sub">Your Journey</p>
    <ul class="abs contact-list">
      <li>Phone : 831 / 555 - 0147</li>
      <li>Fax &nbsp;&nbsp;&nbsp;: 831 / 555 - 0147</li>
      <li>dean.valcourt@vantortraining.example</li>
      <li>Ridgeline Ave Halden Creek, CA 90000</li>
    </ul>
    <p class="abs contact-web">www.vantortraining.example</p>
  </article>

  <article class="panel panel--services">
    <div class="abs intro-box">
      <h2>Performing at high level is getting about better every day</h2>
      <p>When it comes to improving health and performance, a one-size-fits-all approach fits no one well. That why we’ve created a platform for achievement that goes beyond sport performance, corporate fitness, or traditional health care. We’re connecting people to the things that are vital to their health - the ingredients they need to perform at high level day after day</p>
    </div>
    <ol class="abs service-list">
      <li>1. Baseball Specific Performance Training</li>
      <li>2. Physical Therapy</li>
      <li>3. Nutrition</li>
    </ol>
    <div class="abs tools-band"></div>
    <h2 class="abs tools-title">Training Geared for your 5 tools</h2>
    <ul class="abs tools-list">
      <li>Hitting for Average</li>
      <li>Hitting for Power</li>
      <li>Throwing Ability</li>
      <li>Fielding Ability</li>
      <li>Running Speed</li>
    </ul>
    <p class="abs tools-copy">Our training baseball include everything an athlete needs to prepare for the season and become five tool player. Start with personal assessment to identify strength, weakness, and injury risk. After a personal interview to go over assessment result and goles, step into a completely customized training program that includes once or twice-per-day training to adress body composition total body power, baseball specific speed, and pain, and injury prevention.</p>
  </article>

  <article class="panel panel--what-we-do">
    <h2 class="abs wwd-title">WHAT WE DO</h2>
    <p class="abs wwd-intro">Baseball Overview : Baseball is a game that used force in every aspect of movements perform on the field, wheter is sprinting, throwing, or hitting.<br>A generic program will not properly prepare you for the season, so specified program will result as the most beneficial to train.<br>Restoring mobility in the off-seasons is very important, especially because the repetitiveness of baseball, the body become very asymmetrical, so restoring mobility and movement is important to getting your ready for the next season.</p>

    <p class="abs wwd-tagline">At VANTOR’S training we believe in setting attainable athletics goals for<br><strong>MAXIMUM RESULT.</strong></p>
    <div class="abs batter-art" role="img" aria-label="Illustration of a batter mid-swing with strength, power and explosiveness callouts"></div>

    <div class="abs pillar pillar--strength">
      <div class="letters"><span>S</span><span>T</span><span>R</span><span>E</span><span>N</span><span>G</span><span>T</span><span>H</span></div>
      <ul>
        <li>In baseball, the end-goal is NOT bulk and size or even maximal strength- the main adjective is to develop explosive power</li>
        <li>Increased strength alone won’t make a dramatic impact on your performance. Being able to apply that strength quickly will.</li>
      </ul>
    </div>

    <div class="abs pillar pillar--power">
      <div class="letters"><span>P</span><span>O</span><span>W</span><span>E</span><span>R</span></div>
      <p>Training for power should not to be the first phase of your training plan. You must establish a strong base and stability before working on power.<br>Power in the most basic of formula is strength plus speed. It is the combination of these two entities cohesively working together that allow a sprinter to sprint fast, a pitcher to throw hard, and hitter to swing with power. The scientific definition of power statesit is the ability to generate great amount of force</p>
    </div>

    <div class="abs pillar pillar--explosive">
      <div class="letters"><span>E</span><span>X</span><span>P</span><span>L</span><span>O</span><span>S</span><span>I</span><span>V</span><span>E</span><span>N</span><span>E</span><span>S</span><span>S</span></div>
      <ul>
        <li>To be able to keep up with increasing performance standards, players must train to be explosive. And to improve explosiveness, players have to train explosively.</li>
        <li>No training method will perfectly replicate an actual baseball game, but training should mimic what players is required do over and over</li>
      </ul>
    </div>
  </article>
</section>

</body>
</html>
```